BOLD & MINIMALIST DESIGN NEEDED

We want a very bold but minimalistic business card design that is impactful and utilizes both sides of the business card. Our current logo is included for your use.

We want bold fonts and good use of negative space. We don't want the logo to overpower the design.

Target Market(s)

Professionals who are building new commercial buildings.

Industry/Entity Type

Construction

Contact Information for Business Card

Name, Title, email, office phone, cell phone, website

Font styles to use
Serif
Sans Serif

Requirements
Must have
• Bold design!

```html
<!DOCTYPE html>
<html lang="en">
<head>
<meta charset="utf-8">
<title>Ridgeline Design + Build — Business Card</title>
<link rel="stylesheet" href="https://fonts.googleapis.com/css2?family=Lato:wght@400;700;900&display=swap">
<style>
  :root {
    --backdrop: #2a2a2a;
    --paper: #ffffff;
    --ink: #111111;
    --green-light: #9ccc52;
    --green-mid: #6fa521;
    --green-deep: #2f4f0b;
    --green-back: #4f7d16;
    --text-on-green: #ffffff;
  }
  * { box-sizing: border-box; margin: 0; padding: 0; }
  html, body {
    width: 1200px; height: 800px; overflow: hidden;
    background: var(--backdrop);
    font-family: "Lato", Arial, sans-serif;
  }
  .stage { position: relative; width: 1200px; height: 800px; }
  .card {
    position: absolute; left: 320px;
    width: 560px; height: 320px;
    border-radius: 18px; overflow: hidden;
  }
  .card--front { top: 55px; background: var(--paper); }
  .card--back {
    top: 425px;
    background: radial-gradient(ellipse at 55% 35%, var(--green-mid) 0%, var(--green-back) 40%, var(--green-deep) 100%);
  }
  .card__wave { position: absolute; inset: 0; width: 100%; height: 100%; }

  .brand {
    position: absolute; display: flex; align-items: center; gap: 10px;
    font-weight: 900; text-transform: uppercase; line-height: 1;
  }
  .brand__name span { display: block; white-space: nowrap; }
  .brand__mark { width: 22px; height: 22px; flex: none; }
  .brand--front { left: 34px; top: 60px; color: var(--ink); font-size: 24px; letter-spacing: 0.5px; }
  .brand--front .brand__mark { background: var(--green-mid); }
  .brand--back {
    inset: 0; justify-content: center; gap: 18px;
    color: var(--text-on-green); font-size: 40px; letter-spacing: 1px;
  }
  .brand--back .brand__name { line-height: 1.05; }
  .brand--back .brand__mark { width: 34px; height: 34px; border-radius: 50%; background: var(--text-on-green); }

  .holder { position: absolute; left: 40px; top: 196px; color: var(--text-on-green); }
  .holder__name { font-weight: 900; font-size: 25px; line-height: 1.05; }
  .holder__title { font-size: 14px; margin-bottom: 8px; }
  .contact-list { list-style: none; font-size: 14px; line-height: 1.45; }
  .contact-list li { display: flex; align-items: center; gap: 8px; white-space: nowrap; }
  .contact-list svg { width: 12px; height: 12px; fill: var(--text-on-green); flex: none; }

  .office {
    position: absolute; right: 32px; top: 132px; text-align: right;
    color: var(--text-on-green); font-size: 14px; line-height: 1.3;
  }
  .office__web { display: flex; align-items: center; justify-content: flex-end; gap: 8px; margin-top: 14px; }
  .office__web svg { width: 13px; height: 13px; }
</style>
</head>
<body>
<main class="stage">

  <section class="card card--front" aria-label="Business card front">
    <svg class="card__wave" viewBox="0 0 560 320" preserveAspectRatio="none" aria-hidden="true">
      <defs>
        <linearGradient id="greenBand" x1="0" y1="1" x2="1" y2="0">
          <stop offset="0" stop-color="#5f9a18"/>
          <stop offset="0.6" stop-color="#7fb52e"/>
          <stop offset="1" stop-color="#a3d05a"/>
        </linearGradient>
      </defs>
      <path d="M0,178 C110,205 210,198 300,150 C390,100 470,60 560,70 L560,320 L0,320 Z" fill="url(#greenBand)"/>
      <path d="M0,170 C110,196 205,185 295,135 C385,85 470,50 520,52 C470,58 395,95 305,148 C215,200 110,206 0,178 Z" fill="#111"/>
    </svg>

    <div class="brand brand--front">
      <span class="brand__mark"></span>
      <span class="brand__name"><span>Ridgeline</span><span>Design + Build</span></span>
    </div>

    <div class="holder">
      <p class="holder__name">Marcus Hale</p>
      <p class="holder__title">Founder &amp; CEO</p>
      <ul class="contact-list">
        <li><svg viewBox="0 0 12 12"><path d="M1,4 Q6,0 11,4 L10,6 L8,5 L8,4 Q6,3 4,4 L4,5 L2,6 Z M2,7 H10 V11 H2 Z"/></svg>012-555-610-204</li>
        <li><svg viewBox="0 0 12 12"><path d="M3,0 H9 A1,1 0 0 1 10,1 V11 A1,1 0 0 1 9,12 H3 A1,1 0 0 1 2,11 V1 A1,1 0 0 1 3,0 Z M3.5,1.5 V9.5 H8.5 V1.5 Z"/></svg>044-555-218-937</li>
        <li><svg viewBox="0 0 12 12"><path d="M0,6 L12,0 L8,12 L6,7 Z"/></svg>hello@ridgelinebuild.com</li>
      </ul>
    </div>

    <div class="office">
      <p>4471 Harbor View Rd Suite 12,</p>
      <p>FL 32540</p>
      <p class="office__web">
        <svg viewBox="0 0 12 12" fill="none" stroke="#fff" stroke-width="1.2"><circle cx="6" cy="6" r="5"/><ellipse cx="6" cy="6" rx="2.2" ry="5"/><path d="M1,6 H11"/></svg>
        www.ridgelinebuild.com
      </p>
    </div>
  </section>

  <section class="card card--back" aria-label="Business card back">
    <div class="brand brand--back">
      <span class="brand__mark"></span>
      <span class="brand__name"><span>Ridgeline</span><span>Design + Build</span></span>
    </div>
  </section>

</main>
</body>
</html>
```